Graphic to hang inside of fitness studio

This graphic will be printed on vinyl and hung inside of a boutique fitness studio for 2019. Graphic should read YEAR OF POSSIBILITIES.

2018 was called Year of Living Well. We would like something on trend for 2019 to hang within the studio as our 2019 Mantra. It is not a logo but for internal use. I've attached our logo here and the website is www.quillenmovehall.com for additional reference. Thank you.

Target Market(s)

25 to 45 women

Industry/Entity Type

Fitness

Colors

Designer to choose colors to be used in the design.

Requirements
Must have
• On trend for 2019. (no people in image)
• Year of Possibilities in trendy font.
• Easy to read.
• Need text only.
• Do not need graphic images.
Nice to have
• Tintavo colours for 2019
• 2019 design trends for background
Should not have
• Male dominate colour or masculine traits.
• Photos of fitness.
• Photos of people.
• Photos of equipment.

```html
<!DOCTYPE html>
<html lang="en">
<head>
<meta charset="utf-8">
<title>Year of Possibilities – Quillen Move Hall</title>
<link rel="stylesheet" href="https://fonts.googleapis.com/css2?family=Fira+Sans+Condensed:wght@300;800&display=swap">
<style>
  :root {
    --red-core: #e41b24;
    --red-edge: #c1262e;
    --white: #ffffff;
    --fold-light: #f4f4f4;
    --fold-shade: #a9a9a9;
  }
  html, body {
    margin: 0;
    padding: 0;
    overflow: hidden;
  }
  .mantra-banner {
    position: relative;
    width: 1200px;
    height: 600px;
    overflow: hidden;
    background: radial-gradient(ellipse 60% 70% at 50% 50%, var(--red-core) 0%, var(--red-edge) 100%);
    font-family: "Fira Sans Condensed", "Arial Narrow", sans-serif;
  }
  .studio-name {
    position: absolute;
    top: 44px;
    left: 0;
    width: 100%;
    margin: 0;
    text-align: center;
    color: var(--white);
    font-weight: 300;
    font-size: 22px;
    letter-spacing: 0.18em;
    text-transform: uppercase;
  }
  .headline {
    position: absolute;
    inset: 0;
    width: 1200px;
    height: 600px;
  }
  .headline-text {
    font-family: "Fira Sans Condensed", "Arial Narrow", sans-serif;
    font-weight: 800;
    font-size: 156px;
    text-transform: uppercase;
  }
</style>
</head>
<body>
  <main class="mantra-banner">
    <p class="studio-name">Quillen Move Hall</p>

    <svg class="headline" viewBox="0 0 1200 600" xmlns="http://www.w3.org/2000/svg" role="heading" aria-level="1" aria-label="Year of Possibilities">
      <defs>
        <linearGradient id="fold-fill" x1="0" y1="0" x2="0" y2="1">
          <stop offset="0%" stop-color="var(--fold-light)"/>
          <stop offset="60%" stop-color="#dcdcdc"/>
          <stop offset="100%" stop-color="var(--fold-shade)"/>
        </linearGradient>
        <clipPath id="upper-slice">
          <rect x="0" y="0" width="1200" height="270"/>
        </clipPath>
        <clipPath id="lower-slice">
          <rect x="0" y="270" width="1200" height="330"/>
        </clipPath>
      </defs>
      <g transform="rotate(-2.6 600 300)">
        <g clip-path="url(#lower-slice)">
          <text class="headline-text" x="600" y="348" text-anchor="middle" fill="var(--white)" textLength="1090" lengthAdjust="spacingAndGlyphs">Year of Possibilities</text>
        </g>
        <g clip-path="url(#upper-slice)">
          <text class="headline-text" x="598" y="345" text-anchor="middle" fill="url(#fold-fill)" textLength="1090" lengthAdjust="spacingAndGlyphs" aria-hidden="true">Year of Possibilities</text>
        </g>
      </g>
    </svg>
  </main>
</body>
</html>
```